high-impact, conversion-focused website redesign for the government sector

Objective: To design and develop a high-impact, conversion-focused digital platform that solidifies Harrowgate Lumen Advisors (HLA) as the leading communications and strategy firm for government, defense, and industrial clients. The site must project authority, innovation, and sophisticated precision. See the creative breif for more information

Target Market(s)

Government contractors

Industry/Entity Type

Government, defense, industrials

Coding

Coded - Design and coding required

Number of Pages Required

5+ page

Font styles to use
Other font styles liked:
• See the current website

Requirements
Must have
• See design brief
Nice to have
• See design brief
Should not have
• See design brief

```html
<!DOCTYPE html>
<html lang="en">
<head>
<meta charset="utf-8">
<title>Harrowgate Lumen Advisors — Accelerate Your Mission</title>
<link href="https://fonts.googleapis.com/css2?family=Michroma&family=Montserrat:wght@400;500;600&display=swap" rel="stylesheet">
<style>
:root{
  --navy-900:#050d18;
  --navy-800:#0a1a2c;
  --navy-700:#0f2640;
  --steel:#3a5a7a;
  --paper:#f3f5f7;
  --ink:#0b1a2b;
  --muted:#5b6673;
  --line:#c9d0d8;
  --white:#ffffff;
  --accent:#2f8fd8;
}
*{box-sizing:border-box;margin:0;padding:0}
html,body{width:1200px;height:4744px;overflow:hidden}
body{font-family:"Montserrat",Arial,sans-serif;background:var(--paper);color:var(--ink)}
.display{font-family:"Michroma","Arial Black",sans-serif;font-weight:400;letter-spacing:.04em}
section,header,footer{position:relative;width:1200px}
.abs{position:absolute}
.btn{display:inline-flex;align-items:center;gap:10px;font-size:11px;font-weight:600;letter-spacing:.08em;text-transform:uppercase;padding:9px 16px;border:1px solid currentColor;color:var(--white)}
.btn.dark{color:var(--ink)}
.btn svg{width:14px;height:10px}

/* hero */
.hero{height:1000px;background:var(--navy-900);overflow:hidden;color:var(--white)}
.hero-art{position:absolute;inset:0;background:radial-gradient(ellipse at 62% 30%,#2a4f74 0%,#102640 35%,transparent 65%),radial-gradient(ellipse at 92% 40%,rgba(210,80,40,.45) 0%,transparent 35%),linear-gradient(180deg,#0b1c30 0%,#06101c 100%)}
.nav{position:absolute;top:0;left:0;width:1200px;height:64px;display:flex;align-items:center;padding:0 64px;font-size:11px;font-weight:500;letter-spacing:.06em;text-transform:uppercase}
.nav-left,.nav-right{display:flex;gap:28px;align-items:center;flex:1}
.nav-right{justify-content:flex-end}
.nav a{color:var(--white);text-decoration:none}
.nav a.active{color:var(--accent)}
.brand{display:flex;align-items:center;gap:10px;font-family:"Montserrat",sans-serif;font-weight:600;font-size:14px;letter-spacing:.08em;text-transform:uppercase;color:var(--white)}
.brand i{width:14px;height:14px;background:var(--accent);display:block}
.hero-title{left:60px;top:150px;font-size:82px;line-height:1.08;text-transform:uppercase}
.hero-title .outline{color:transparent;-webkit-text-stroke:1.4px var(--white)}
.hero-lede{left:62px;top:472px;width:520px;font-size:17px;line-height:1.5}
.hero-cta{left:62px;top:560px}
.stats{left:0;top:760px;width:1200px;height:220px}
.stat{position:absolute;top:50px;width:260px;text-align:center}
.stat b{display:block;font-family:"Michroma",sans-serif;font-weight:400;font-size:30px;margin-bottom:18px}
.stat span{font-size:10px;line-height:1.5;color:#c9d6e4;display:block}

/* services */
.services{height:1432px;background:var(--paper)}
.section-title{font-size:40px;text-transform:uppercase;text-align:center;color:var(--ink)}
.services .section-title{position:absolute;top:1076px;top:76px;width:100%}
.services-intro{top:166px;left:270px;width:660px;text-align:center;font-size:13px;line-height:1.6;color:var(--muted)}
.feature{left:72px;top:240px;width:1056px;height:352px;background:linear-gradient(120deg,#4a3a32 0%,#8d7a6c 30%,#c9c2bb 55%,#5b6a7a 80%,#2c3440 100%);color:var(--white)}
.feature::after{content:"";position:absolute;inset:0;background:linear-gradient(0deg,rgba(5,13,24,.75) 0%,transparent 55%)}
.feature-text{position:absolute;left:24px;bottom:24px;z-index:1}
.feature-text h3{font-size:28px;font-weight:500;margin-bottom:8px}
.feature-text p{font-size:13px}
.feature svg{position:absolute;right:24px;bottom:28px;z-index:1;width:30px;height:30px}
.service-list{left:72px;top:600px;width:1056px;list-style:none}
.service-list li{height:96px;display:flex;align-items:center;justify-content:space-between;border-bottom:1px solid var(--line);font-size:28px;font-weight:400;color:#2a3440}
.service-list svg{width:26px;height:18px}
.services .btn{left:532px;top:1362px}

/* expect */
.expect{height:728px;background:linear-gradient(180deg,var(--navy-800),var(--navy-900));color:var(--white)}
.expect h2{left:72px;top:56px;font-size:40px;line-height:1.3;text-transform:uppercase;width:820px}
.expect-lede{left:72px;top:188px;width:880px;font-size:14px;line-height:1.6;color:#cbd6e2}
.expect .btn{left:72px;top:272px}
.step{top:356px;width:248px;height:280px;overflow:hidden}
.step-art{position:absolute;inset:0}
.step::after{content:"";position:absolute;inset:0;background:linear-gradient(0deg,rgba(5,13,24,.9) 0%,transparent 60%)}
.step-text{position:absolute;left:14px;bottom:18px;right:14px;z-index:1}
.step-text h3{font-size:22px;font-weight:500;margin-bottom:6px}
.step-text p{font-size:10px;line-height:1.45;color:#d4dde7}

/* cases */
.cases{height:960px;background:var(--paper)}
.cases h2{left:72px;top:68px;font-size:40px;text-transform:uppercase}
.cases-lede{left:72px;top:140px;font-size:13px;color:var(--muted)}
.project{left:0;top:184px;width:1200px;height:616px;background:radial-gradient(ellipse at 50% 25%,#4d6f8e 0%,#22405e 35%,#0d1e33 75%);color:var(--white);overflow:hidden}
.project-big{position:absolute;top:40px;width:100%;text-align:center;font-family:"Michroma",sans-serif;font-size:118px;line-height:1.05;letter-spacing:.22em;color:rgba(200,215,230,.55)}
.project-art{position:absolute;left:240px;top:260px;width:760px;height:240px;background:radial-gradient(ellipse at 50% 60%,rgba(8,16,28,.85) 0%,rgba(8,16,28,.4) 45%,transparent 70%)}
.project-name{position:absolute;left:64px;bottom:72px;font-size:22px;font-family:"Michroma",sans-serif;text-transform:uppercase}
.project-desc{position:absolute;left:64px;bottom:44px;font-size:12px;color:#cdd8e4}
.project .btn{position:absolute;right:64px;bottom:64px}
.cases .btn.dark{left:500px;top:862px}

/* footer */
.footer{height:624px;background:radial-gradient(ellipse at 50% 100%,#12304f 0%,#07121f 60%);color:var(--white)}
.footer h2{top:70px;width:100%;text-align:center;font-size:30px;text-transform:uppercase}
.footer-lede{top:128px;width:100%;text-align:center;font-size:13px;color:#cdd8e4}
.footer-lede a{color:var(--accent);text-decoration:none}
.footer .brand{left:300px;top:296px;position:absolute}
.fcol{top:252px;font-size:10px;line-height:2;text-transform:uppercase;color:#b9c6d4}
.fcol h4{font-size:12px;font-weight:600;color:var(--white);margin-bottom:4px}
.copyright{top:532px;width:100%;text-align:center;font-size:12px;color:#cdd8e4}
.social{top:570px;left:540px;display:flex;gap:20px}
.social i{width:12px;height:12px;border-radius:50%;border:1px solid #cdd8e4;display:block}
</style>
</head>
<body>

<header class="hero">
  <div class="hero-art" role="img" aria-label="Dusk photograph of a jet aircraft on a launch pad with deep blue sky and warm orange lights"></div>
  <nav class="nav">
    <div class="nav-left"><a class="active" href="#">Home</a><a href="#">Advisory Services</a><a href="#">Blogs</a></div>
    <div class="brand"><i></i>Harrowgate Lumen Advisors</div>
    <div class="nav-right"><a href="#">About Us</a><a class="btn" href="#">Contact Us</a></div>
  </nav>
  <h1 class="abs hero-title display"><span class="outline">Accelerate</span><br><span class="outline">Your</span><br>Mission<sup style="font-size:18px">+</sup></h1>
  <p class="abs hero-lede">Connecting the federal ecosystem with the technologies that matter most to America and her allies.</p>
  <a class="abs btn hero-cta" href="#">Get Started <svg viewBox="0 0 14 10"><path d="M0 5h12M8 1l4 4-4 4" fill="none" stroke="currentColor" stroke-width="1.4"/></svg></a>
  <div class="abs stats">
    <svg width="1200" height="220" viewBox="0 0 1200 220" style="position:absolute;inset:0">
      <polygon points="0,10 380,10 440,0 760,0 820,10 1200,10 1200,210 820,210 760,220 440,220 380,210 0,210" fill="rgba(30,70,110,.45)"/>
      <polygon points="460,0 740,0 780,110 740,220 460,220 420,110" fill="rgba(10,26,44,.85)" stroke="rgba(120,160,200,.4)"/>
    </svg>
    <div class="stat" style="left:150px"><b>+72%</b><span>Increase in database contacts through CRM modernization and targeted outreach campaigns</span></div>
    <div class="stat" style="left:470px"><b>100+</b><span>Introductions to buyers across agencies and the defense and industrial base ecosystem</span></div>
    <div class="stat" style="left:790px"><b>570%</b><span>Increase in pipeline value after strategic repositioning for a federal growth client</span></div>
  </div>
</header>

<section class="services">
  <h2 class="section-title display">Our Services</h2>
  <p class="abs services-intro">We've helped brands strengthen their digital presence, expand their network, and accelerate opportunities across the defense, space, and government sectors. In just one year, our clients have achieved:</p>
  <div class="abs feature" role="img" aria-label="Photograph of business colleagues in discussion around a meeting table">
    <div class="feature-text"><h3>Corporate Communications</h3><p>Collaboration, internal and external messaging, and integrated strategy</p></div>
    <svg viewBox="0 0 30 30"><path d="M4 26L26 4M10 4h16v16" fill="none" stroke="#fff" stroke-width="2"/></svg>
  </div>
  <ul class="abs service-list">
    <li>Public Relations<svg viewBox="0 0 26 18"><path d="M0 9h24M16 1l8 8-8 8" fill="none" stroke="currentColor" stroke-width="1.6"/></svg></li>
    <li>Government Affairs<svg viewBox="0 0 26 18"><path d="M0 9h24M16 1l8 8-8 8" fill="none" stroke="currentColor" stroke-width="1.6"/></svg></li>
    <li>Crisis Communications<svg viewBox="0 0 26 18"><path d="M0 9h24M16 1l8 8-8 8" fill="none" stroke="currentColor" stroke-width="1.6"/></svg></li>
    <li>Digital Marketing<svg viewBox="0 0 26 18"><path d="M0 9h24M16 1l8 8-8 8" fill="none" stroke="currentColor" stroke-width="1.6"/></svg></li>
    <li>Strategic Connections<svg viewBox="0 0 26 18"><path d="M0 9h24M16 1l8 8-8 8" fill="none" stroke="currentColor" stroke-width="1.6"/></svg></li>
    <li>Investor Relations<svg viewBox="0 0 26 18"><path d="M0 9h24M16 1l8 8-8 8" fill="none" stroke="currentColor" stroke-width="1.6"/></svg></li>
    <li>Event Management<svg viewBox="0 0 26 18"><path d="M0 9h24M16 1l8 8-8 8" fill="none" stroke="currentColor" stroke-width="1.6"/></svg></li>
  </ul>
  <a class="abs btn dark" href="#">Learn More <svg viewBox="0 0 14 10"><path d="M0 5h12M8 1l4 4-4 4" fill="none" stroke="currentColor" stroke-width="1.4"/></svg></a>
</section>

<section class="expect">
  <h2 class="abs display">What to Expect When Partnering With Us</h2>
  <p class="abs expect-lede">We combine deep federal sector insight, technical understanding, and a powerful network across government, industry, investors, and media. Our proven approach drives results — from major contract wins and successful M&amp;A to increased valuation, strategic investment, and political support.</p>
  <a class="abs btn" href="#">Get Started <svg viewBox="0 0 14 10"><path d="M0 5h12M8 1l4 4-4 4" fill="none" stroke="currentColor" stroke-width="1.4"/></svg></a>
  <div class="abs step" style="left:56px"><div class="step-art" role="img" aria-label="Photograph of executives in a boardroom discussion" style="background:linear-gradient(150deg,#6b5a48,#2a2a2c 60%,#141820)"></div><div class="step-text"><h3>Discovery</h3><p>Deep dive into your mission, goals, challenges, and market position.</p></div></div>
  <div class="abs step" style="left:376px"><div class="step-art" role="img" aria-label="Photograph of a strategy meeting with laptops" style="background:linear-gradient(150deg,#8a8478,#3e4a56 55%,#151c26)"></div><div class="step-text"><h3>Strategy</h3><p>Custom and tailored plans built to align messaging with your objectives.</p></div></div>
  <div class="abs step" style="left:636px"><div class="step-art" role="img" aria-label="Photograph of hands working on documents and a tablet" style="background:linear-gradient(150deg,#a9a39a,#4b5058 55%,#141a22)"></div><div class="step-text"><h3>Execution</h3><p>Precise implementation with attention to every detail.</p></div></div>
  <div class="abs step" style="left:896px"><div class="step-art" role="img" aria-label="Photograph of a tablet showing performance charts" style="background:linear-gradient(150deg,#3f6a8e,#1c3550 55%,#0a1420)"></div><div class="step-text"><h3>Measurement</h3><p>Ongoing performance tracking to show value and guide growth.</p></div></div>
</section>

<section class="cases">
  <h2 class="abs display">Featured Case Studies</h2>
  <p class="abs cases-lede">Check out some of our latest successful projects.</p>
  <div class="abs project">
    <div class="project-big">PROJECT<br>NAME</div>
    <div class="project-art" role="img" aria-label="Photograph of a military transport aircraft in flight through clouds"></div>
    <div class="project-name">Project Name</div>
    <p class="project-desc">Enter a short and important details about this project.</p>
    <a class="btn" href="#">Learn More <svg viewBox="0 0 14 10"><path d="M0 5h12M8 1l4 4-4 4" fill="none" stroke="currentColor" stroke-width="1.4"/></svg></a>
  </div>
  <a class="abs btn dark" href="#">View Our Latest Work <svg viewBox="0 0 14 10"><path d="M0 5h12M8 1l4 4-4 4" fill="none" stroke="currentColor" stroke-width="1.4"/></svg></a>
</section>

<footer class="footer">
  <h2 class="abs display">Ignite Your Strategy</h2>
  <p class="abs footer-lede">For any inquiries, questions, or mind-blowing ideas, drop us a line at <a href="#">hello@harrowgatelumen.example</a></p>
  <div class="brand"><i></i>Harrowgate Lumen Advisors</div>
  <div class="abs fcol" style="left:612px"><h4>Quick Links</h4>Home<br>Advisory Services<br>About Us<br>Blogs</div>
  <div class="abs fcol" style="left:808px"><h4>Services</h4>Corporate Communications<br>Public Relations<br>Government Affairs<br>Crisis Communications<br>Digital Marketing</div>
  <p class="abs copyright">Copyright © 2025 Harrowgate Lumen Advisors.</p>
  <div class="abs social" aria-label="Social links"><i></i><i></i><i></i><i></i><i></i></div>
</footer>

</body>
</html>
```